Marlow Brochure

Brevik & Solan Education Group was formed in 2011 as an organizational arm
to put educational and charitable services together for community
development.

B & S was acquired by Marlow Education Group in 2013 and relocated to Texas
with the expressed focus of reaching underserved communities and
population, both in the Dallas- Fort Worth Metropolitan area and Houston
areas. Key members of the organization are based in Dallas, TX, Houston,
TX, Atlanta GA, and Washington DC and are strategically networked to
utilize their external resources for education advancement with
under-served populations.

Target Market(s)

- -The target market is 17-45 year olds, the demographics are 70%
women, 30% men, interested in an entry level education in
the health field

Industry/Entity Type

Education

```html
<!DOCTYPE html>
<html lang="en">
<head>
<meta charset="utf-8">
<title>Marlow Brochure</title>
<link href="https://fonts.googleapis.com/css2?family=Didact+Gothic&family=Nunito:wght@700;800&display=swap" rel="stylesheet">
<style>
  :root {
    --page: #ffffff;
    --stage: #ffffff;
    --ink: #111111;
    --muted: #6f6f6f;
    --green-1: #e4efc6;
    --green-2: #d6e8a8;
    --green-3: #eef5dc;
    --brand: #2a7fb6;
    --photo-grey-a: #d9d9d9;
    --photo-grey-b: #9a9a9a;
    --photo-tan-a: #e6dcc6;
    --photo-tan-b: #8a7a5c;
    --photo-pink-a: #f2e9ea;
    --photo-pink-b: #b7475f;
  }
  * { margin: 0; padding: 0; box-sizing: border-box; }
  html, body { width: 1200px; height: 1000px; overflow: hidden; background: var(--stage); }
  body { position: relative; font-family: "Didact Gothic", "Helvetica Neue", Arial, sans-serif; color: var(--ink); }

  .brochure {
    position: absolute; left: 0; top: 75px; width: 1200px; height: 850px;
    background: var(--page); overflow: hidden;
    box-shadow: 0 2px 4px rgba(0,0,0,0.18);
  }
  .bands { position: absolute; inset: 0; }

  .photo { position: absolute; }
  .photo--aide { left: 0; top: 0; width: 245px; height: 295px;
    background: linear-gradient(160deg, var(--photo-grey-a), #f2f2f2 55%, var(--photo-grey-b)); opacity: .85; }
  .photo--desk { left: 800px; top: 0; width: 400px; height: 397px;
    background: linear-gradient(150deg, #3a3328 0%, var(--photo-tan-b) 18%, var(--photo-tan-a) 55%, #cbbd9d 100%); }
  .photo--notebook { left: 401px; top: 632px; width: 399px; height: 215px;
    background: linear-gradient(170deg, var(--photo-pink-a) 0%, #e9e2e0 60%, var(--photo-pink-b) 100%); }

  .brand { position: absolute; left: 262px; top: 58px; display: flex; align-items: center; gap: 6px;
    font-size: 13px; color: var(--brand); }
  .brand-dot { width: 12px; height: 12px; border-radius: 50%; background: var(--brand); }

  .intro { position: absolute; left: 30px; top: 318px; width: 340px; }
  .intro h1 { font-family: "Nunito", Arial, sans-serif; font-weight: 800; font-size: 24px; line-height: 26px; }
  .intro p { margin-top: 6px; font-size: 13px; line-height: 20px; color: var(--muted); }
  .intro p + p { margin-top: 20px; }

  .services { position: absolute; font-size: 15px; line-height: 19.9px; color: #222; }
  .services h2 { font-family: "Nunito", Arial, sans-serif; font-weight: 700; font-size: 14.5px; line-height: 20px; color: var(--ink); }
  .services ul { list-style: none; }
  .services li::before { content: "• "; }
  .services--medical { left: 428px; top: 42px; width: 340px; }
  .services--medical h2 { padding-left: 3px; }
  .services--patient { left: 428px; top: 280px; }
  .services--home { left: 602px; top: 283px; }
  .services--other { left: 428px; top: 479px; }

  .contact { position: absolute; left: 38px; top: 668px; list-style: none; font-size: 15px; }
  .contact li { display: flex; align-items: center; height: 37px; }
  .contact svg { width: 32px; height: 26px; margin-right: 9px; fill: var(--ink); }

  .history { position: absolute; left: 829px; top: 422px; width: 345px; }
  .history h2 { font-family: "Nunito", Arial, sans-serif; font-weight: 800; font-size: 29px; line-height: 36px; }
  .history p { font-size: 12.5px; line-height: 21.4px; color: #333; }
</style>
</head>
<body>
<main class="brochure">
  <svg class="bands" viewBox="0 0 1200 850" preserveAspectRatio="none" aria-hidden="true">
    <polygon fill="var(--green-1)" points="0,238 800,80 800,397 1200,397 1200,850 1200,850 800,730 0,585"/>
    <polygon fill="var(--green-2)" opacity=".55" points="0,238 800,80 800,190 0,300"/>
    <polygon fill="var(--green-3)" opacity=".7" points="0,520 800,460 800,560 0,585"/>
    <polygon fill="var(--green-2)" opacity=".45" points="800,420 1200,470 1200,560 800,520"/>
    <polygon fill="var(--green-3)" opacity=".8" points="800,660 1200,740 1200,850 820,850"/>
    <polygon fill="var(--page)" points="0,585 400,715 400,850 0,850"/>
  </svg>

  <div class="photo photo--aide" role="img" aria-label="Black and white portrait of a smiling home health aide in scrubs"></div>
  <div class="photo photo--desk" role="img" aria-label="Eyeglasses and a pen resting on a stack of papers"></div>
  <div class="photo photo--notebook" role="img" aria-label="Close-up of a spiral notebook with a pink pen"></div>

  <div class="brand"><span class="brand-dot"></span>Marlow Education Group</div>

  <section class="intro">
    <h1>Is the Home Health Aide Certification Important?</h1>
    <p>If you are serious about a career in health care, the answer is absolutely yes!</p>
    <p>A Home Health Aide certification means you will have more job options, career<br>flexibility, and you will earn more money! &nbsp;Take the time and build a stronger<br>foundation for you career!</p>
  </section>

  <section class="services services--medical">
    <h2>Medical care</h2>
    <ul>
      <li>Checking Vital Signs (e.g., blood pressure, pulse, temperature, respiration, glucose)</li>
      <li>Assisting with Medications</li>
      <li>Changing Bandages</li>
      <li>Exercise Therapy Assistance</li>
      <li>Knowledge of Diseases and Illnesses</li>
      <li>Infection Control</li>
      <li>Measuring Fluid Outtake/Intake</li>
      <li>Colostomy or Catheter Care</li>
      <li>Monitoring Patients</li>
    </ul>
  </section>
  <section class="services services--patient">
    <h2>Patient care</h2>
    <ul>
      <li>Bathing</li><li>Oral Hygiene</li><li>Dressing</li><li>Skincare</li>
      <li>Grooming</li><li>Shaving</li><li>Ambulation</li><li>Feeding</li>
    </ul>
  </section>
  <section class="services services--home">
    <h2>Home Making</h2>
    <ul>
      <li>Cooking</li><li>Bed Changes</li><li>Laundry</li><li>Cleaning</li><li>Dusting</li><li>Shopping</li>
    </ul>
  </section>
  <section class="services services--other">
    <h2>Other</h2>
    <ul>
      <li>Record Keeping</li><li>Running Errands</li><li>Transporting to Appointments</li>
      <li>Entertaining Patient</li><li>Companionship Training</li>
    </ul>
  </section>

  <ul class="contact">
    <li><svg viewBox="0 0 32 26"><rect x="1" y="4" width="30" height="19"/><polyline points="1,4 16,15 31,4" fill="none" stroke="#fff" stroke-width="2"/></svg>www.marlowed@mailbox.com</li>
    <li><svg viewBox="0 0 32 26"><g fill="none" stroke="#111" stroke-width="1.8"><circle cx="16" cy="13" r="11"/><ellipse cx="16" cy="13" rx="5" ry="11"/><line x1="5" y1="13" x2="27" y2="13"/><line x1="7" y1="7" x2="25" y2="7"/><line x1="7" y1="19" x2="25" y2="19"/></g></svg>www.MarlowEd.com</li>
    <li><svg viewBox="0 0 32 26"><rect x="9" y="0" width="14" height="26" rx="2"/><rect x="11" y="3" width="10" height="17" fill="#fff"/></svg>000-0000000</li>
    <li><svg viewBox="0 0 32 26"><path d="M16 0a8 8 0 0 1 8 8c0 6-8 18-8 18S8 14 8 8a8 8 0 0 1 8-8z"/><circle cx="16" cy="8" r="3" fill="#fff"/></svg>Your Adresss, Comes to,Here</li>
  </ul>

  <section class="history">
    <h2>History</h2>
    <p>Brevik &amp; Solan Education Group was formed in 2011 as an organizational arm to put educational and charitable services together for underserved communities. In the process Brevik &amp; Solan was able to facilitate educational programs for non-profit entities in the state of including for single-mothers seeking employment and workers seeking job search retraining.<br>
    B &amp; S was acquired by Marlow Education Group in 2013 and relocated to Texas with the expressed focus of reaching underserved communities and population, both in the Dallas- Fort Worth Metropolitan area and Houston areas. Key members of the organization are based in Dallas, TX, Houston, TX and Washington DC and are strategically networked to utilize their external resources for education advancement with under-served populations.</p>
  </section>
</main>
</body>
</html>
```